Tamarind Lodgings letterhead

We need a letterhead designed that includes the new logo that has just been designed for our business. The letterhead will need to be formatted for digital use as well as for print.

Target Market(s)

Private tenant, corporate tenants, real estate agents

Industry/Entity Type

Digital

Requirements
Must have
• ABN 58 907 412 336
PO Box 8163, Coral Bend Mail Centre QLD 4762
Email: marlow.pike@inboxnest.com
Ph: 0437 592 064

```html
<!DOCTYPE html>
<html lang="en">
<head>
<meta charset="utf-8">
<title>Tamarind Lodgings Letterhead</title>
<link href="https://fonts.googleapis.com/css2?family=Comfortaa:wght@500;700&display=swap" rel="stylesheet">
<style>
  :root {
    --band: #5a0c24;
    --brand: #7c2a2c;
    --rule: #d3323f;
    --paper: #ffffff;
    --ghost: #f6f3f4;
  }
  html, body {
    margin: 0;
    padding: 0;
    overflow: hidden;
    background: var(--paper);
  }
  .letterhead {
    position: relative;
    width: 867px;
    height: 1200px;
    background: var(--paper);
    overflow: hidden;
    font-family: "Comfortaa", sans-serif;
  }
  .side-band {
    position: absolute;
    left: 0;
    top: 0;
    width: 107px;
    height: 100%;
    background: var(--band);
  }
  .brand {
    position: absolute;
    left: 124px;
    top: 30px;
    display: flex;
    align-items: center;
    gap: 14px;
  }
  .brand-mark {
    width: 66px;
    height: 66px;
    background: var(--band);
    border-radius: 6px;
  }
  .brand-name {
    margin: 0;
    font-weight: 700;
    font-size: 27px;
    line-height: 1.05;
    letter-spacing: 0.5px;
    color: var(--brand);
    text-transform: uppercase;
  }
  .contact {
    position: absolute;
    left: 492px;
    top: 33px;
    margin: 0;
    font-style: normal;
    font-weight: 500;
    font-size: 19px;
    line-height: 25px;
    color: var(--brand);
  }
  .contact span { display: block; }
  .header-rule {
    position: absolute;
    left: 107px;
    right: 0;
    top: 181px;
    height: 3px;
    background: var(--rule);
  }
  .ghost-square {
    position: absolute;
    left: 270px;
    top: 600px;
    width: 520px;
    height: 520px;
    background: var(--ghost);
    border-radius: 60px;
    transform: rotate(-12deg);
  }
</style>
</head>
<body>
  <div class="letterhead">
    <div class="side-band"></div>
    <div class="ghost-square"></div>

    <div class="brand">
      <div class="brand-mark"></div>
      <p class="brand-name">Tamarind<br>Lodgings</p>
    </div>

    <address class="contact">
      <span>ABN 58 907 412 336</span>
      <span>PO BOX 8163 , Coral Bend Mail Centre</span>
      <span>QLD 4762</span>
      <span>EMAIL : marlow.pike@inboxnest.com</span>
      <span>PHONE : 0437 592 064</span>
    </address>

    <div class="header-rule"></div>
  </div>
</body>
</html>
```